Halvern Guildworks Business Cards
Need out-of-the-box business card design
Halvern Guildworks Business Cards -
Creative Brief
Modern
Peter Strandquell
5172 Orrin St. Denver, CO 80219
peter@halvernguildworks.com
halvernguildworks.com
We exist to foster healthy artist Community, create points of Collaboration and provide tangible benefit to local Causes.

```html
<!DOCTYPE html>
<html lang="en">
<head>
<meta charset="utf-8">
<title>Halvern Guildworks Business Cards</title>
<link rel="stylesheet" href="https://fonts.googleapis.com/css2?family=Ubuntu:wght@400&family=Crimson+Text:wght@400;700&display=swap">
<style>
  :root {
    --backdrop: #e9e6e1;
    --card: #ffffff;
    --band-light: #c9a43a;
    --band-dark: #9c7a22;
    --leaf: #7f9a2a;
    --leaf-light: #a7bd4a;
    --brand: #8a6a1c;
    --ink: #4a4438;
    --rule: #cfc8b8;
  }
  * { margin: 0; padding: 0; box-sizing: border-box; }
  html, body { width: 1200px; height: 852px; overflow: hidden; }
  body { background: var(--backdrop); position: relative; }

  .card {
    position: absolute;
    width: 560px;
    height: 320px;
    background: var(--card);
    border-radius: 22px;
    overflow: hidden;
    box-shadow: 0 8px 22px rgba(0,0,0,.18);
  }
  .card--stacked { left: 130px; top: 80px; }
  .card--split { left: 510px; top: 452px; }

  .card__band { position: absolute; inset: 0 0 auto 0; width: 560px; height: 130px; }

  .card__name {
    position: absolute; right: 34px; top: 18px;
    font-family: "Crimson Text", serif; font-weight: 700;
    font-size: 22px; color: #fff; letter-spacing: .2px;
  }

  .brand {
    position: absolute; left: 40px; top: 120px;
    display: flex; align-items: center; gap: 14px;
  }
  .brand__dot { width: 38px; height: 38px; border-radius: 50%; background: var(--band-light); }
  .brand__name {
    font-family: "Ubuntu", sans-serif; font-weight: 400;
    font-size: 40px; line-height: .95; color: var(--brand);
  }
  .brand__name span { display: block; font-size: 26px; }

  .details { font-family: "Crimson Text", serif; font-size: 14px; color: var(--ink); line-height: 1.3; }
  .address { position: absolute; }
  .contacts { position: absolute; list-style: none; }
  .contacts li { display: flex; align-items: center; gap: 8px; }
  .contacts svg { width: 12px; height: 12px; flex: none; }

  .card--stacked .address { left: 40px; top: 210px; }
  .card--stacked .contacts { left: 40px; top: 255px; }

  .card--split .brand { left: 90px; top: 128px; }
  .card--split .address { left: 90px; top: 236px; text-align: right; width: 120px; left: 60px; }
  .card--split .divider { position: absolute; left: 200px; top: 222px; width: 1px; height: 70px; background: var(--rule); }
  .card--split .contacts { left: 214px; top: 226px; }
</style>
</head>
<body>

<svg width="0" height="0" style="position:absolute">
  <defs>
    <linearGradient id="band-fill" x1="0" y1="0" x2="1" y2="0">
      <stop offset="0" stop-color="var(--band-dark)"/>
      <stop offset=".55" stop-color="var(--band-light)"/>
      <stop offset="1" stop-color="var(--band-dark)"/>
    </linearGradient>
    <symbol id="icon-phone" viewBox="0 0 12 12"><path d="M3 1 L5 3 L4 4.5 Q5.5 7 7.5 8 L9 7 L11 9 L9.5 11 Q3 10 1 2.5 Z" fill="var(--band-dark)"/></symbol>
    <symbol id="icon-mail" viewBox="0 0 12 12"><rect x="1" y="2.5" width="10" height="7" fill="var(--band-dark)"/><path d="M1 2.5 L6 7 L11 2.5" stroke="#fff" fill="none" stroke-width=".9"/></symbol>
    <symbol id="icon-web" viewBox="0 0 12 12"><circle cx="6" cy="6" r="5" fill="var(--band-light)"/><path d="M1 6 H11 M6 1 Q3 6 6 11 Q9 6 6 1" stroke="#fff" fill="none" stroke-width=".8"/></symbol>
  </defs>
</svg>

<article class="card card--stacked">
  <svg class="card__band" viewBox="0 0 560 130" aria-hidden="true">
    <path d="M0 0 H560 V58 Q330 48 150 78 Q60 94 0 112 Z" fill="url(#band-fill)"/>
    <path d="M150 80 Q330 52 560 60 V74 Q360 62 150 80 Z" fill="var(--leaf)"/>
    <path d="M260 70 Q400 60 560 74 V80 Q400 68 260 70 Z" fill="var(--leaf-light)"/>
  </svg>
  <p class="card__name">Peter Strandquell</p>
  <div class="brand">
    <span class="brand__dot"></span>
    <p class="brand__name">halvern<span>guildworks</span></p>
  </div>
  <p class="details address">5172 Orrin St.<br>Denver, CO 80219</p>
  <ul class="details contacts">
    <li><svg><use href="#icon-phone"/></svg>3035550148</li>
    <li><svg><use href="#icon-mail"/></svg>peter@halvernguildworks.com</li>
    <li><svg><use href="#icon-web"/></svg>www.halvernguildworks.com</li>
  </ul>
</article>

<article class="card card--split">
  <svg class="card__band" viewBox="0 0 560 130" aria-hidden="true">
    <path d="M0 0 H560 V58 Q330 48 150 78 Q60 94 0 112 Z" fill="url(#band-fill)"/>
    <path d="M150 80 Q330 52 560 60 V74 Q360 62 150 80 Z" fill="var(--leaf)"/>
    <path d="M260 70 Q400 60 560 74 V80 Q400 68 260 70 Z" fill="var(--leaf-light)"/>
  </svg>
  <p class="card__name">Peter Strandquell</p>
  <div class="brand">
    <span class="brand__dot"></span>
    <p class="brand__name">halvern<span>guildworks</span></p>
  </div>
  <p class="details address">5172 Orrin St.<br>Denver, CO 80219</p>
  <span class="divider"></span>
  <ul class="details contacts">
    <li><svg><use href="#icon-phone"/></svg>3035550148</li>
    <li><svg><use href="#icon-mail"/></svg>peter@halvernguildworks.com</li>
    <li><svg><use href="#icon-web"/></svg>www.halvernguildworks.com</li>
  </ul>
</article>

</body>
</html>
```